We require a banner design for a 53' x 10' trailer for a future development to be displayed on the side of the highway. The development name is 712 35 Commerce Park, logo is attached. This is an industrial future development. Please also include the RLW Group logo and MERO Development logos as well.

Industry/Entity Type

Real Estate / Construction / Developer / Industrial Future Development

Requirements
Must have
• Logos provided

```html
<!DOCTYPE html>
<html lang="en">
<head>
<meta charset="utf-8">
<title>712 35 Commerce Park – Future Industrial Development</title>
<link rel="stylesheet" href="https://fonts.googleapis.com/css2?family=Montserrat:wght@400;500;600;700;800&display=swap">
<style>
  :root {
    --page-bg: #e4e5e7;
    --banner-white: #ffffff;
    --banner-blue: #6b8bd2;
    --banner-blue-deep: #5573bd;
    --ink: #1d1a1a;
    --brown: #5e4b43;
    --photo-warm: #9a8b7c;
    --photo-cool: #6f8fb8;
    --accent-red: #d8323a;
    --accent-blue: #1f4da0;
  }
  html, body {
    margin: 0;
    padding: 0;
    overflow: hidden;
    background: var(--page-bg);
  }
  .canvas {
    width: 1200px;
    height: 660px;
    position: relative;
    background: var(--page-bg);
    overflow: hidden;
  }
  .trailer-banner {
    position: absolute;
    left: 20px;
    top: 221px;
    width: 1160px;
    height: 218px;
    box-shadow: 4px 5px 8px rgba(0,0,0,0.28);
    display: block;
  }
  .park-number {
    font-family: "Montserrat", sans-serif;
    font-weight: 800;
    font-size: 50px;
    fill: var(--ink);
  }
  .park-label {
    font-family: "Montserrat", sans-serif;
    font-weight: 500;
    font-size: 14px;
    letter-spacing: 1.6px;
    fill: var(--ink);
  }
  .partner-name {
    font-family: "Montserrat", sans-serif;
    font-weight: 700;
    font-size: 10px;
    fill: var(--ink);
  }
  .headline {
    font-family: "Montserrat", sans-serif;
    font-weight: 800;
    font-size: 118px;
    fill: var(--banner-white);
  }
  .tagline {
    font-family: "Montserrat", sans-serif;
    font-weight: 600;
    font-size: 31px;
    fill: var(--banner-white);
  }
</style>
</head>
<body>
<div class="canvas">
  <svg class="trailer-banner" viewBox="0 0 1160 218" xmlns="http://www.w3.org/2000/svg">
    <defs>
      <clipPath id="banner-clip"><rect width="1160" height="218"/></clipPath>
      <linearGradient id="collage-tones" x1="0" y1="0" x2="1" y2="1">
        <stop offset="0" stop-color="var(--photo-warm)"/>
        <stop offset="1" stop-color="var(--photo-cool)"/>
      </linearGradient>
    </defs>
    <g clip-path="url(#banner-clip)">
      <rect class="backdrop" width="1160" height="218" fill="var(--banner-blue)" role="img" aria-label="Faint photo of an industrial refinery in blue tones"/>

      <g class="chevrons" fill="none" stroke="var(--banner-blue-deep)" stroke-width="2.5">
        <polyline points="862,14 870,20 862,26"/>
        <polyline points="869,14 877,20 869,26"/>
        <polyline points="876,14 884,20 876,26"/>
        <polyline points="282,184 290,190 282,196"/>
        <polyline points="289,184 297,190 289,196"/>
        <polyline points="296,184 304,190 296,196"/>
      </g>

      <g class="panel-left">
        <ellipse cx="42" cy="109" rx="244" ry="176" fill="var(--banner-white)"/>
        <ellipse cx="42" cy="109" rx="236" ry="168" fill="var(--ink)"/>
        <ellipse cx="42" cy="109" rx="228" ry="160" fill="var(--banner-white)"/>
      </g>

      <g class="panel-right">
        <ellipse cx="1125" cy="109" rx="244" ry="176" fill="var(--banner-white)"/>
        <ellipse cx="1125" cy="109" rx="236" ry="168" fill="var(--ink)"/>
        <ellipse cx="1125" cy="109" rx="228" ry="160" fill="var(--banner-white)"/>
      </g>

      <g class="park-name">
        <text class="park-number" x="46" y="72" textLength="151" lengthAdjust="spacingAndGlyphs">712</text>
        <text class="park-number" x="97" y="119" textLength="100" lengthAdjust="spacingAndGlyphs">35</text>
        <text class="park-label" x="121" y="144" text-anchor="middle">COMMERCE PARK</text>
      </g>

      <g class="partners">
        <rect x="36" y="172" width="9" height="9" fill="var(--accent-red)"/>
        <text class="partner-name" x="49" y="181" textLength="96" lengthAdjust="spacingAndGlyphs">MERO Development</text>
        <line x1="153" y1="168" x2="153" y2="188" stroke="var(--ink)" stroke-width="1"/>
        <circle cx="165" cy="177" r="4.5" fill="var(--accent-blue)"/>
        <text class="partner-name" x="174" y="181" textLength="58" lengthAdjust="spacingAndGlyphs">RLW Group</text>
      </g>

      <text class="headline" x="581" y="123" text-anchor="middle">FUTURE</text>
      <rect class="tagline-pill" x="332" y="142" width="498" height="46" rx="23" fill="var(--brown)"/>
      <text class="tagline" x="581" y="176" text-anchor="middle">INDUSTRIAL DEVELOPMENT</text>

      <rect class="photo-collage" x="948" y="17" width="188" height="185" rx="22" fill="url(#collage-tones)" role="img" aria-label="Collage of industrial photos: storage tanks, factory floor worker, engineers reviewing plans, power plant stacks"/>
    </g>
  </svg>
</div>
</body>
</html>
```